2019/20 Season Calendar (This is to be at the top of the calendar as title)

An advertising calendar for our agricultural business to explain our key business attributes and give clients a nice looking calendar to refer to .

Please refer to doc/pdf attachments for text details and ideas. (Our current logo needs to be incorporated - this logo can be altered if need be)

open to professional agriculture aesthetics keeping in line with the companies Green colour scheme (logo)

The calendar is to start at October 2019 - September 2020

97mm x 122mm

Target Market(s)

Agricultural sector (professional)

Industry/Entity Type

Agriculture

Font styles to use
Sans Serif

Colors
abd036
3276b5

Requirements
Must have
• Calender with dates starting october 1st 2019 finishing end of september 2020.
• Must include all public holidays etc for Australia during this time.
• contact details including website :www.brevardholdings.com.au
Nice to have
• In the calendar the months of
• October/ nov /december (be coloured yellow)
• April/May/June (be coloured brown)
• July /aug/september (be coloured green)
• Jan/feb/march (be coloured white)
• Then in the corner of the calendar a key (like a map) to refer to the colours
• [a small square with the colour yellow] (next to the square the following text) Harvesting
• [a small square with the colour brown] (next to the square the following text) Sowing
• [a small square with the colour green] (next to the square the following text) Growing
• [a small square with the colour white] (next to the square the following text) Liming + Fertilising

```html
<!DOCTYPE html>
<html lang="en">
<head>
<meta charset="utf-8">
<title>Brevard Holdings – 2019/20 Season Calendar</title>
<link href="https://fonts.googleapis.com/css2?family=Lilita+One&family=Open+Sans:wght@300;400;600;700&family=Ubuntu:wght@500;700&display=swap" rel="stylesheet">
<style>
:root{
  --blue:#3276b5;
  --lime:#abd036;
  --harvest:#ffe100;
  --sow:#5b3b1f;
  --grow:#2cb36d;
  --band:#3f8f3c;
  --band-dark:#2f7430;
  --ink:#1d1d1b;
  --title:#ffe100;
  --white:#ffffff;
}
*{margin:0;padding:0;box-sizing:border-box}
html,body{width:954px;height:1200px;overflow:hidden;background:var(--white)}
.canvas{position:relative;width:954px;height:1200px;overflow:hidden;background:var(--white);font-family:"Open Sans",sans-serif;color:var(--ink)}

.field{position:absolute;left:18px;top:470px;width:936px;height:430px;
  background:linear-gradient(180deg,rgba(255,255,255,1) 0%,#e9efc9 30%,#cdd98e 65%,#b6c46a 100%)}

.brand{position:absolute;left:47px;top:36px;display:flex;align-items:center;gap:8px}
.brand-mark{width:22px;height:22px;background:var(--ink)}
.brand-name{font-family:"Ubuntu",sans-serif;font-weight:700;font-size:17px;line-height:19px;color:var(--ink);text-transform:uppercase}

.title{position:absolute;left:234px;top:30px;font-family:"Lilita One",sans-serif;font-size:52px;letter-spacing:1px;color:var(--title);
  -webkit-text-stroke:2px #3a3a2a;paint-order:stroke fill}

.quarter{position:absolute;left:37px;width:593px;height:187px;background:rgba(255,255,255,.72);border:1.5px solid}
.q-harvest{top:102px;border-color:var(--harvest)}
.q-lime{top:295px;border-color:var(--ink)}
.q-sow{top:487px;border-color:var(--sow)}
.q-grow{top:679px;border-color:var(--grow)}
.season{position:absolute;left:0;top:0;width:27px;height:100%;display:flex;align-items:center;justify-content:center}
.season span{transform:rotate(-90deg);white-space:nowrap;font-size:11px;font-weight:700;font-variant:small-caps;letter-spacing:.5px;font-size:13px}
.q-harvest .season{background:var(--harvest)} .q-harvest .season span{color:var(--ink)}
.q-lime .season{background:var(--white);border-right:1.5px solid var(--ink)} .q-lime .season span{color:var(--ink)}
.q-sow .season{background:var(--sow)} .q-sow .season span{color:var(--white)}
.q-grow .season{background:var(--grow)} .q-grow .season span{color:var(--white)}

.month{position:absolute;top:16px;width:163px}
.m1{left:37px}.m2{left:227px}.m3{left:418px}
.mhead{height:23px;background:var(--blue);color:var(--white);display:flex;justify-content:space-between;align-items:center;padding:0 8px 0 4px}
.mname{font-size:18px;font-weight:400;letter-spacing:.3px}
.myear{font-size:11px;font-weight:700}
.days{display:grid;grid-template-columns:repeat(7,1fr);grid-auto-rows:20.5px;margin-top:3px;font-size:12.5px;text-align:center;align-items:center}
.days span{line-height:17px}
.days .h{color:var(--ink)}
.days .hs,.days .s{color:var(--blue)}
.days .g{background:var(--lime);color:var(--ink)}
.days .b{background:var(--blue);color:var(--white)}

.holidays{position:absolute;left:653px;top:121px;width:300px;font-size:17.5px;line-height:25px;font-weight:300;white-space:nowrap}
.hol-head{width:243px;height:27px;background:var(--blue);color:var(--white);text-align:center;font-variant:small-caps;font-size:19px;line-height:27px;font-weight:400}
.hol-kind{display:flex;align-items:center;gap:10px;font-variant:small-caps;font-size:18px}
.hol-kind i{display:block;width:12px;height:12px}
.k-public{color:var(--lime)} .k-public i{background:var(--lime)}
.k-school{color:var(--blue)} .k-school i{background:var(--blue)}
.holidays b{font-weight:600}

.band{position:absolute;left:0;top:899px;width:954px;height:301px;background:linear-gradient(180deg,#b7c25a 0%,var(--band) 6%,var(--band) 70%,var(--band-dark) 100%)}
.yard-photo{position:absolute;left:48px;top:945px;width:277px;height:152px;border:2px solid var(--white);
  background:linear-gradient(180deg,#8fb6dc 0%,#c9dcec 45%,#9aa3a8 75%,#6f7a62 100%)}
.services{position:absolute;left:347px;top:933px;width:560px;font-family:"Ubuntu",sans-serif}
.services h2{font-weight:700;font-size:25px;color:var(--title);letter-spacing:.3px;-webkit-text-stroke:1.5px #2a2a1a;paint-order:stroke fill;margin-bottom:4px}
.services ul{list-style:none;color:var(--white);font-size:20.5px;font-weight:500;line-height:27.5px}
.services li{position:relative;padding-left:28px}
.services li::before{content:"";position:absolute;left:8px;top:9px;width:10px;height:10px;border-radius:50%;background:var(--title)}
.rule{position:absolute;left:28px;top:1119px;width:888px;height:2px;background:var(--title)}
.contact{position:absolute;top:1132px;font-family:"Ubuntu",sans-serif;font-weight:500;font-size:18.5px;line-height:25px;color:var(--white);display:flex;gap:8px}
.contact svg{flex:none;margin-top:1px}
.c-addr{left:46px}.c-mail{left:404px}.c-phone{left:757px}
</style>
</head>
<body>
<div class="canvas">
  <div class="field" role="img" aria-label="Soft photo of green wheat paddocks under a pale sky"></div>

  <div class="brand"><span class="brand-mark"></span><span class="brand-name">Brevard<br>Holdings</span></div>
  <h1 class="title">2019/20 SEASON CALENDAR</h1>

  <!-- Harvesting -->
  <section class="quarter q-harvest">
    <div class="season"><span>Harvesting</span></div>
    <div class="month m1"><div class="mhead"><span class="mname">OCTOBER</span><span class="myear">2019</span></div>
      <div class="days"><span class="hs">Su</span><span class="h">Mo</span><span class="h">Tu</span><span class="h">We</span><span class="h">Th</span><span class="h">Fr</span><span class="h">Sa</span>
        <span style="grid-column-start:3">1</span><span>2</span><span>3</span><span>4</span><span>5</span>
        <span class="s">6</span><span class="g">7</span><span>8</span><span>9</span><span>10</span><span>11</span><span>12</span>
        <span class="b">13</span><span>14</span><span>15</span><span>16</span><span>17</span><span>18</span><span>19</span>
        <span class="s">20</span><span>21</span><span>22</span><span>23</span><span>24</span><span>25</span><span>26</span>
        <span class="s">27</span><span>28</span><span>29</span><span>30</span><span>31</span></div></div>
    <div class="month m2"><div class="mhead"><span class="mname">NOVEMBER</span><span class="myear">2019</span></div>
      <div class="days"><span class="hs">Su</span><span class="h">Mo</span><span class="h">Tu</span><span class="h">We</span><span class="h">Th</span><span class="h">Fr</span><span class="h">Sa</span>
        <span style="grid-column-start:6">1</span><span>2</span>
        <span class="s">3</span><span>4</span><span>5</span><span>6</span><span>7</span><span>8</span><span>9</span>
        <span class="s">10</span><span>11</span><span>12</span><span>13</span><span>14</span><span>15</span><span>16</span>
        <span class="s">17</span><span>18</span><span>19</span><span>20</span><span>21</span><span>22</span><span>23</span>
        <span class="s">24</span><span>25</span><span>26</span><span>27</span><span>28</span><span>29</span><span>30</span></div></div>
    <div class="month m3"><div class="mhead"><span class="mname">DECEMBER</span><span class="myear">2019</span></div>
      <div class="days"><span class="hs">Su</span><span class="h">Mo</span><span class="h">Tu</span><span class="h">We</span><span class="h">Th</span><span class="h">Fr</span><span class="h">Sa</span>
        <span class="s">1</span><span>2</span><span>3</span><span>4</span><span>5</span><span>6</span><span>7</span>
        <span class="s">8</span><span>9</span><span>10</span><span>11</span><span>12</span><span>13</span><span>14</span>
        <span class="s">15</span><span>16</span><span>17</span><span>18</span><span>19</span><span>20</span><span class="b">21</span>
        <span class="s">22</span><span>23</span><span>24</span><span class="g">25</span><span class="g">26</span><span>27</span><span>28</span>
        <span class="s">29</span><span>30</span><span>31</span></div></div>
  </section>

  <!-- Liming + Fertilising -->
  <section class="quarter q-lime">
    <div class="season"><span>Liming + Fertilising</span></div>
    <div class="month m1"><div class="mhead"><span class="mname">JANUARY</span><span class="myear">2020</span></div>
      <div class="days"><span class="hs">Su</span><span class="h">Mo</span><span class="h">Tu</span><span class="h">We</span><span class="h">Th</span><span class="h">Fr</span><span class="h">Sa</span>
        <span class="g" style="grid-column-start:4">1</span><span>2</span><span>3</span><span>4</span>
        <span class="s">5</span><span>6</span><span>7</span><span>8</span><span>9</span><span>10</span><span>11</span>
        <span class="s">12</span><span>13</span><span>14</span><span>15</span><span>16</span><span>17</span><span>18</span>
        <span class="s">19</span><span>20</span><span>21</span><span>22</span><span>23</span><span>24</span><span>25</span>
        <span class="s">26</span><span class="g">27</span><span>28</span><span>29</span><span>30</span><span>31</span></div></div>
    <div class="month m2"><div class="mhead"><span class="mname">FEBRUARY</span><span class="myear">2020</span></div>
      <div class="days"><span class="hs">Su</span><span class="h">Mo</span><span class="h">Tu</span><span class="h">We</span><span class="h">Th</span><span class="h">Fr</span><span class="h">Sa</span>
        <span style="grid-column-start:7">1</span>
        <span class="s">2</span><span>3</span><span>4</span><span>5</span><span>6</span><span>7</span><span>8</span>
        <span class="s">9</span><span>10</span><span>11</span><span>12</span><span>13</span><span>14</span><span>15</span>
        <span class="s">16</span><span>17</span><span>18</span><span>19</span><span>20</span><span>21</span><span>22</span>
        <span class="s">23</span><span>24</span><span>25</span><span>26</span><span>27</span><span>28</span><span>29</span></div></div>
    <div class="month m3"><div class="mhead"><span class="mname">MARCH</span><span class="myear">2020</span></div>
      <div class="days"><span class="hs">Su</span><span class="h">Mo</span><span class="h">Tu</span><span class="h">We</span><span class="h">Th</span><span class="h">Fr</span><span class="h">Sa</span>
        <span class="s">1</span><span>2</span><span>3</span><span>4</span><span>5</span><span>6</span><span>7</span>
        <span class="s">8</span><span>9</span><span>10</span><span>11</span><span>12</span><span>13</span><span>14</span>
        <span class="s">15</span><span>16</span><span>17</span><span>18</span><span>19</span><span>20</span><span>21</span>
        <span class="s">22</span><span>23</span><span>24</span><span>25</span><span>26</span><span>27</span><span>28</span>
        <span class="s">29</span><span>30</span><span>31</span></div></div>
  </section>

  <!-- Sowing -->
  <section class="quarter q-sow">
    <div class="season"><span>Sowing</span></div>
    <div class="month m1"><div class="mhead"><span class="mname">APRIL</span><span class="myear">2020</span></div>
      <div class="days"><span class="hs">Su</span><span class="h">Mo</span><span class="h">Tu</span><span class="h">We</span><span class="h">Th</span><span class="h">Fr</span><span class="h">Sa</span>
        <span style="grid-column-start:4">1</span><span>2</span><span>3</span><span>4</span>
        <span class="s">5</span><span>6</span><span>7</span><span>8</span><span>9</span><span class="g">10</span><span class="g">11</span>
        <span class="g">12</span><span class="g">13</span><span class="b">14</span><span class="b">15</span><span class="b">16</span><span class="b">17</span><span class="b">18</span>
        <span class="b">19</span><span class="b">20</span><span class="b">21</span><span class="b">22</span><span class="b">23</span><span class="b">24</span><span class="g">25</span>
        <span class="b">26</span><span class="b">27</span><span>28</span><span>29</span><span>30</span></div></div>
    <div class="month m2"><div class="mhead"><span class="mname">MAY</span><span class="myear">2020</span></div>
      <div class="days"><span class="hs">Su</span><span class="h">Mo</span><span class="h">Tu</span><span class="h">We</span><span class="h">Th</span><span class="h">Fr</span><span class="h">Sa</span>
        <span style="grid-column-start:6">1</span><span>2</span>
        <span class="s">3</span><span>4</span><span>5</span><span>6</span><span>7</span><span>8</span><span>9</span>
        <span class="s">10</span><span>11</span><span>12</span><span>13</span><span>14</span><span>15</span><span>16</span>
        <span class="s">17</span><span>18</span><span>19</span><span>20</span><span>21</span><span>22</span><span>23</span>
        <span class="s">24</span><span>25</span><span>26</span><span>27</span><span>28</span><span>29</span><span>30</span>
        <span class="s">31</span></div></div>
    <div class="month m3"><div class="mhead"><span class="mname">JUNE</span><span class="myear">2020</span></div>
      <div class="days"><span class="hs">Su</span><span class="h">Mo</span><span class="h">Tu</span><span class="h">We</span><span class="h">Th</span><span class="h">Fr</span><span class="h">Sa</span>
        <span style="grid-column-start:2">1</span><span>2</span><span>3</span><span>4</span><span>5</span><span>6</span>
        <span class="s">7</span><span class="g">8</span><span>9</span><span>10</span><span>11</span><span>12</span><span>13</span>
        <span class="s">14</span><span>15</span><span>16</span><span>17</span><span>18</span><span>19</span><span>20</span>
        <span class="s">21</span><span>22</span><span>23</span><span>24</span><span>25</span><span>26</span><span>27</span>
        <span class="s">28</span><span>29</span><span>30</span></div></div>
  </section>

  <!-- Growing -->
  <section class="quarter q-grow">
    <div class="season"><span>Growing</span></div>
    <div class="month m1"><div class="mhead"><span class="mname">JULY</span><span class="myear">2020</span></div>
      <div class="days"><span class="hs">Su</span><span class="h">Mo</span><span class="h">Tu</span><span class="h">We</span><span class="h">Th</span><span class="h">Fr</span><span class="h">Sa</span>
        <span style="grid-column-start:4">1</span><span>2</span><span>3</span><span class="b">4</span>
        <span class="b">5</span><span class="b">6</span><span class="b">7</span><span class="b">8</span><span class="b">9</span><span class="b">10</span><span class="b">11</span>
        <span class="b">12</span><span class="b">13</span><span class="b">14</span><span class="b">15</span><span class="b">16</span><span class="b">17</span><span class="b">18</span>
        <span class="b">19</span><span class="b">20</span><span>21</span><span>22</span><span>23</span><span>24</span><span>25</span>
        <span class="s">26</span><span>27</span><span>28</span><span>29</span><span>30</span><span>31</span></div></div>
    <div class="month m2"><div class="mhead"><span class="mname">AUGUST</span><span class="myear">2020</span></div>
      <div class="days"><span class="hs">Su</span><span class="h">Mo</span><span class="h">Tu</span><span class="h">We</span><span class="h">Th</span><span class="h">Fr</span><span class="h">Sa</span>
        <span style="grid-column-start:7">1</span>
        <span class="s">2</span><span class="g">3</span><span>4</span><span>5</span><span>6</span><span>7</span><span>8</span>
        <span class="s">9</span><span>10</span><span>11</span><span>12</span><span>13</span><span>14</span><span>15</span>
        <span class="s">16</span><span>17</span><span>18</span><span>19</span><span>20</span><span>21</span><span>22</span>
        <span class="s">23</span><span>24</span><span>25</span><span>26</span><span>27</span><span>28</span><span>29</span>
        <span class="s">30</span><span>31</span></div></div>
    <div class="month m3"><div class="mhead"><span class="mname">SEPTEMBER</span><span class="myear">2020</span></div>
      <div class="days"><span class="hs">Su</span><span class="h">Mo</span><span class="h">Tu</span><span class="h">We</span><span class="h">Th</span><span class="h">Fr</span><span class="h">Sa</span>
        <span style="grid-column-start:3">1</span><span>2</span><span>3</span><span>4</span><span>5</span>
        <span class="s">6</span><span>7</span><span>8</span><span>9</span><span>10</span><span>11</span><span>12</span>
        <span class="s">13</span><span>14</span><span>15</span><span>16</span><span>17</span><span>18</span><span>19</span>
        <span class="s">20</span><span>21</span><span>22</span><span>23</span><span>24</span><span>25</span><span class="b">26</span>
        <span class="b">27</span><span class="g">28</span><span class="b">29</span><span class="b">30</span></div></div>
  </section>

  <aside class="holidays">
    <div class="hol-head">Holidays 2019</div>
    <div class="hol-kind k-public" style="margin-top:13px"><i></i>Public Holidays</div>
    <div><b>7 October</b> - Labour Day</div>
    <div><b>25 December</b>- Christmas Day</div>
    <div><b>26 December</b>- Boxing Day</div>
    <div class="hol-kind k-school" style="margin-top:13px"><i></i>School Holidays</div>
    <div><b>13 October</b>- School Holidays</div>
    <div><b>21 December</b> - School Holidays -<br>Western Division</div>
    <div class="hol-head" style="margin-top:9px">Holidays 2020</div>
    <div class="hol-kind k-public" style="margin-top:6px"><i></i>Public Holidays</div>
    <div><b>1 January</b> - New Year's Day</div>
    <div><b>27 January</b> - Australia Day</div>
    <div><b>10 April</b> - Good Friday</div>
    <div><b>11 April</b> - Easter Saturday (the<br>Saturday following Good Friday)</div>
    <div><b>12 April</b> - Easter Sunday</div>
    <div><b>13 April</b> - Easter Monday</div>
    <div><b>25 April</b> - Anzac Day</div>
    <div><b>8 June</b> - Queen's Birthday</div>
    <div><b>3 August</b> - Bank Holiday</div>
    <div class="hol-kind k-school" style="margin-top:7px"><i></i>School Holidays</div>
    <div><b>10 April- 27 April</b> -<br>Autumn Holidays</div>
    <div><b>4 July- 20 July</b> - Winter Holidays</div>
    <div><b>26 September- 11 October</b> -<br>Spring Holidays</div>
  </aside>

  <div class="band">
  </div>
  <div class="yard-photo" role="img" aria-label="Photo of the grain storage yard with sheds, silos and a truck"></div>
  <div class="services">
    <h2>GRAIN - FERTILISER - TRANSPORT - STORAGE</h2>
    <ul>
      <li>Buy and sell grain + stock feed at great prices</li>
      <li>Buy fertiliser / lime / gypsum (when you need it)</li>
      <li>Store or sell your grain at harvest (to access<br>when you need to - daily cash prices on website)</li>
      <li>Move your bulk goods across NSW , VIC, QLD &amp; SA</li>
    </ul>
  </div>
  <div class="rule"></div>
  <div class="contact c-addr">
    <svg width="22" height="24" viewBox="0 0 22 24"><circle cx="11" cy="11" r="10" fill="#fff"/><path d="M11 4a4.5 4.5 0 0 0-4.5 4.5C6.5 12 11 17 11 17s4.5-5 4.5-8.5A4.5 4.5 0 0 0 11 4z" fill="#3f8f3c"/><circle cx="11" cy="8.5" r="1.7" fill="#fff"/></svg>
    <span>42 Railway Parade - Tallowa NSW 2671<br>Australia</span>
  </div>
  <div class="contact c-mail">
    <svg width="22" height="24" viewBox="0 0 22 24"><circle cx="11" cy="11" r="10" fill="#fff"/><rect x="5" y="7" width="12" height="8.5" fill="none" stroke="#3f8f3c" stroke-width="1.5"/><path d="M5 7l6 5 6-5" fill="none" stroke="#3f8f3c" stroke-width="1.5"/></svg>
    <span>admin@brevardholdings.com.au</span>
  </div>
  <div class="contact c-phone">
    <svg width="22" height="24" viewBox="0 0 22 24"><circle cx="11" cy="11" r="10" fill="#fff"/><path d="M7.5 6.5c-.8.8-.8 2.6.9 4.9s3.6 3.7 5.3 3.8c.9 0 1.6-.6 1.8-1.2l-2-1.6-1.1.9c-.8-.4-2-1.6-2.5-2.5l.9-1.1-1.6-2z" fill="#3f8f3c"/></svg>
    <span>02 6900 4318</span>
  </div>
</div>
</body>
</html>
```